SpinReel Needs a 1 Page Redesign with UI/UX Elements

SpinReel is a GIF creation and sharing site. We are upgrading one of our main responsive website pages. [Please see: http://spinreel.net/P-8UQu for an example]

Need design versions for Desktop, tablet & mobile.

Also need frontend development to implement page. Currently on Foundation framework.

There are many functions/nav elements that need to be on this page in an uncluttered and clear manner. Not all of functions need to be shown at all times. Need a designer with UI/UX background to incorporate these and make it easy to navigate for the user.

The designer needs to be familiar with the site to understand each function. Color scheme will remain the same as current site.

If there are Dropdowns/collapsed or hidden features - need to know how they look when opened.

Target Market(s)

SpinReel has a varied demographic but focuses on under 25.

Coding

Coded - Design and coding required

Number of Pages Required

1 page

Font styles to use
Sans Serif

Requirements
Must have
• The top and bottom nav bars must stay the same. We are not redesigning the whole site yet, just that page.
• This page is developed with sharing in mind. Our top 3 actions are highlighted below. Be creative & think about user experience as our #1 priority
• Desktop
•  SOCIAL SHARE BUTTONS Chatterloft/Quillpost/Yarnboard/Clipmosaic
•  Download Button
•  Create a GIF Button
• OTHER FEATURES THAT MUST BE INCLUDED
• Share This With Friends pop up
• Title of GIF
• Added XX days ago by XXXX in XXX
• Source
• Thumbs up votes showing numerically (no down vote thumb)
• Total Views
• Embed Links: direct, website, message board, markdown
• NSFW Flag
• MP4 to GIF toggle
• Next arrows to scroll through GIFs
• Scroll thumbnail bar for like GIFs at the bottom of the page
• NEW FEATURES TO IMPLEMENT
• Favorite (bookmark Option)
• LOGGED IN USERS:
• Logged in users also have Private Button & Delete Button
• MOBILE
• We would like to keep the mobile page as minimalist as possible.
• Download button
• Create a GIF button
• Sharing button: Lumiframe, Chatterloft, Quillpost, Yarnboard,
• Share Via SMS
• (Please incorporate the share buttons in a creative & clean way)
• Three dots that would open up to reveal tags
• Thumbnail scroll at bottom for GIFs in the same category
Nice to have
• Be creative with how the page features are laid out. We want it to be easy for users to navigate & clear what actions are there.
Should not have
• Basically anything that is on the page now. The buttons don't look like buttons & there is no drive to any actions (like sharing). Please see attached file for what NOT to do.

```html
<!DOCTYPE html>
<html lang="en">
<head>
<meta charset="utf-8">
<title>SpinReel – Curbsidez GIF</title>
<link href="https://fonts.googleapis.com/css2?family=Open+Sans:wght@400;600;700;800&display=swap" rel="stylesheet">
<style>
:root{
  --ink:#1f1f1f;
  --bar:#262626;
  --panel:#2b2b2b;
  --panel-line:#3a3a3a;
  --gold:#f5c21b;
  --text:#333;
  --muted:#8a8a8a;
  --line:#e2e2e2;
  --foot:#eeeeee;
  --white:#fff;
  --c1:#3b5998;--c2:#2aa9e0;--c3:#d34836;--c4:#c8232c;--c5:#2e7bd6;--c6:#e0462e;
}
*{box-sizing:border-box;margin:0;padding:0}
html,body{width:811px;height:1200px;overflow:hidden}
body{font-family:"Open Sans",Arial,sans-serif;color:var(--text);background:var(--white);position:relative}
a{color:inherit;text-decoration:none}

.site-header{position:absolute;left:0;top:0;width:811px;height:46px;background:var(--bar);display:flex;align-items:center;padding:0 22px}
.brand{display:flex;align-items:center;gap:6px;color:var(--white);font-weight:700;font-size:15px;margin-right:26px}
.brand-mark{width:16px;height:16px;background:var(--gold)}
.main-nav{display:flex;gap:14px;font-size:8px;font-weight:700;color:#d6d6d6;letter-spacing:.3px;white-space:nowrap}
.header-actions{margin-left:auto;display:flex;align-items:center;gap:8px}
.btn-login{border:1px solid #bbb;color:var(--white);font-size:8px;font-weight:700;padding:4px 8px}
.btn-signup{background:var(--gold);color:var(--ink);font-size:8px;font-weight:700;padding:5px 8px}

.player{position:absolute;left:68px;top:82px;width:424px;height:300px;background:linear-gradient(135deg,#8e8a86 0%,#c7c1b8 45%,#6c6560 100%)}
.player-arrow{position:absolute;top:132px;width:20px;height:36px}
.player-arrow.prev{left:8px}.player-arrow.next{right:8px}
.action-rail{position:absolute;left:492px;top:82px;width:35px;height:322px;background:var(--ink);display:flex;flex-direction:column}
.action-rail span{flex:1;display:flex;align-items:center;justify-content:center;border-bottom:1px solid #333}

.gif-info{position:absolute;left:527px;top:82px;width:230px;height:300px;background:var(--panel);color:#ddd;padding:12px 14px}
.gif-title{font-size:17px;font-weight:800;color:var(--white);letter-spacing:.5px}
.gif-meta{font-size:7.5px;color:var(--muted);margin-top:18px;display:flex;gap:8px;white-space:nowrap}
.gif-meta b{color:var(--gold);font-weight:600}
.info-row{border-top:1px solid var(--panel-line);padding:9px 0;font-size:7.5px;display:flex;align-items:center;gap:6px;white-space:nowrap}
.info-row .label{font-weight:800;color:var(--white);font-size:8.5px}
.tag{color:#bbb}
.stats{justify-content:flex-end;color:var(--gold);font-weight:600}
.like{background:var(--gold);color:var(--ink);font-weight:700;padding:3px 6px}
.source-link{color:var(--gold)}
.private-link{font-size:7px;color:var(--gold);text-align:right;margin-top:2px;white-space:nowrap}

.cta-bar{position:absolute;left:527px;top:382px;width:230px;height:22px;display:flex}
.btn-download{flex:1;background:#1a1a1a;color:var(--white);font-size:8.5px;font-weight:800;display:flex;align-items:center;justify-content:center;gap:6px}
.btn-create{flex:1;background:var(--gold);color:var(--ink);font-size:8.5px;font-weight:800;display:flex;align-items:center;justify-content:center}

.share-row{position:absolute;left:68px;top:396px;display:flex;gap:5px;align-items:center}
.share-sq{width:22px;height:22px;display:block}
.btn-post{margin-left:18px;background:var(--gold);color:var(--ink);font-size:7.5px;font-weight:800;padding:6px 10px;white-space:nowrap}

.rule{position:absolute;left:68px;width:689px;height:1px;background:var(--line)}

.gallery-title{position:absolute;left:68px;font-size:10px;font-weight:800;color:var(--ink);letter-spacing:.3px}
.gallery-row{position:absolute;left:68px;width:689px;height:82px;display:flex;align-items:center}
.gallery-row .nav-arrow{width:22px;display:flex;justify-content:center}
.thumbs{flex:1;display:flex;justify-content:space-between;padding:0 14px}
.thumb{width:108px;height:82px}

.comment-box{position:absolute;left:68px;top:985px;width:689px;height:66px;border:1px solid var(--line);padding:8px}
.avatar{position:absolute;left:8px;top:8px;width:36px;height:36px;background:#d9dde3}
.comment-input{position:absolute;left:52px;top:8px;right:8px;height:30px;border:1px solid var(--line);font-size:7.5px;color:#aaa;padding:6px}
.plugin-note{position:absolute;left:52px;bottom:7px;font-size:7px;color:var(--muted)}
.btn-comment{position:absolute;right:8px;bottom:6px;background:var(--gold);color:var(--ink);font-size:7.5px;font-weight:800;padding:4px 10px}

.site-footer{position:absolute;left:0;top:1106px;width:811px;height:94px;background:var(--foot);padding:18px 68px}
.footer-links{display:flex;justify-content:space-between;font-size:8px;color:#666;white-space:nowrap}
.footer-links .sep{color:#bbb}
.footer-bottom{margin-top:20px;display:flex;justify-content:space-between;align-items:center;font-size:7.5px;color:var(--muted)}
.footer-social{display:flex;gap:6px}
.footer-social span{width:18px;height:18px;border-radius:50%;display:block}
</style>
</head>
<body>

<header class="site-header">
  <a class="brand" href="#"><span class="brand-mark"></span>SpinReel</a>
  <nav class="main-nav">
    <a href="#">THE GALLERY</a><a href="#">PICTURES TO GIF</a><a href="#">VIDTUBE TO GIF</a><a href="#">UPLOAD A GIF</a><a href="#">VIDEO TO GIF</a><a href="#">WEBCAM TO GIF</a>
  </nav>
  <div class="header-actions">
    <a class="btn-login" href="#">LOG IN</a>
    <a class="btn-signup" href="#">SIGN UP</a>
    <svg width="14" height="14" viewBox="0 0 14 14"><circle cx="6" cy="6" r="4.2" fill="none" stroke="#fff" stroke-width="1.8"/><line x1="9" y1="9" x2="13" y2="13" stroke="#fff" stroke-width="2"/></svg>
  </div>
</header>

<div class="player" role="img" aria-label="Animated GIF: girl in a cap sitting on a skateboard">
  <svg class="player-arrow prev" viewBox="0 0 20 36"><polyline points="16,4 4,18 16,32" fill="none" stroke="#fff" stroke-width="3"/></svg>
  <svg class="player-arrow next" viewBox="0 0 20 36"><polyline points="4,4 16,18 4,32" fill="none" stroke="#fff" stroke-width="3"/></svg>
</div>

<div class="action-rail">
  <span><svg width="12" height="11" viewBox="0 0 12 11"><path d="M6 10.5 1 5.5A2.8 2.8 0 0 1 6 2a2.8 2.8 0 0 1 5 3.5z" fill="#fff"/></svg></span>
  <span><svg width="12" height="12" viewBox="0 0 12 12"><polygon points="6,0.5 7.6,4.2 11.5,4.5 8.5,7.1 9.4,11 6,8.9 2.6,11 3.5,7.1 0.5,4.5 4.4,4.2" fill="#fff"/></svg></span>
  <span><svg width="12" height="12" viewBox="0 0 12 12"><circle cx="3" cy="6" r="1.8" fill="#fff"/><circle cx="9.5" cy="2.5" r="1.8" fill="#fff"/><circle cx="9.5" cy="9.5" r="1.8" fill="#fff"/><path d="M3 6 9.5 2.5M3 6l6.5 3.5" stroke="#fff"/></svg></span>
  <span><svg width="12" height="12" viewBox="0 0 12 12"><rect x="1" y="3" width="7" height="6" fill="#fff"/><polygon points="8,6 11.5,3 11.5,9" fill="#fff"/></svg></span>
  <span><svg width="12" height="12" viewBox="0 0 12 12"><path d="M2 11V1h7l-1.5 2.5L9 6H2" fill="#fff"/></svg></span>
  <span><svg width="12" height="12" viewBox="0 0 12 12"><rect x="2" y="5" width="8" height="6" fill="#fff"/><path d="M3.5 5V3.5a2.5 2.5 0 0 1 5 0V5" fill="none" stroke="#fff" stroke-width="1.3"/></svg></span>
  <span><svg width="12" height="12" viewBox="0 0 12 12"><rect x="3" y="3.5" width="6" height="8" fill="#fff"/><rect x="1.5" y="1.5" width="9" height="1.2" fill="#fff"/></svg></span>
  <span><svg width="12" height="12" viewBox="0 0 12 12"><path d="M2 2l8 4-8 4z" fill="#fff"/></svg></span>
</div>

<section class="gif-info">
  <h1 class="gif-title">CURBSIDEZ</h1>
  <p class="gif-meta"><span>added <b>1 days ago</b></span><span>by <b>reelmaster</b></span><span>in <b>funny gifs</b></span></p>
  <div class="info-row" style="margin-top:12px"><span class="label">TAGS</span><span class="tag">Direct</span><span class="tag">Website</span><span class="tag">Message Board</span><span class="tag">Markdown</span></div>
  <div class="info-row stats"><span>1,414 Total Views</span><span class="like">&#9650; 6</span></div>
  <div class="info-row"><span class="label">SOURCE</span><span class="source-link">Watch the full VidTube video</span></div>
  <p class="private-link">Make this GIF private / delete</p>
</section>

<div class="cta-bar">
  <a class="btn-download" href="#"><svg width="9" height="9" viewBox="0 0 9 9"><path d="M4.5 0v6M1.5 3.5l3 3 3-3M0.5 8.5h8" stroke="#fff" fill="none" stroke-width="1.3"/></svg>DOWNLOAD</a>
  <a class="btn-create" href="#">CREATE A GIF</a>
</div>

<div class="share-row">
  <span class="share-sq" style="background:var(--c1)" role="img" aria-label="Share on Chatterloft"></span>
  <span class="share-sq" style="background:var(--c2)" role="img" aria-label="Share on Quillpost"></span>
  <span class="share-sq" style="background:var(--c3)" role="img" aria-label="Share on Orbitcircle"></span>
  <span class="share-sq" style="background:var(--c4)" role="img" aria-label="Share on Clipmosaic"></span>
  <span class="share-sq" style="background:var(--c5)" role="img" aria-label="Share by email"></span>
  <span class="share-sq" style="background:var(--c6)" role="img" aria-label="Share on Yarnboard"></span>
  <a class="btn-post" href="#">ADD YOUR GIF TO CHATTERLOFT</a>
</div>

<div class="rule" style="top:440px"></div>

<h2 class="gallery-title" style="top:462px">CHECK OUT THESE FUNNY GIFS</h2>
<div class="gallery-row" style="top:490px">
  <span class="nav-arrow"><svg width="8" height="14"><polyline points="7,1 1,7 7,13" fill="none" stroke="#777" stroke-width="2"/></svg></span>
  <div class="thumbs">
    <span class="thumb" style="background:linear-gradient(135deg,#5fb6c8,#b9e0e8)" role="img" aria-label="GIF thumbnail: parrot"></span>
    <span class="thumb" style="background:linear-gradient(135deg,#c9b79a,#7c6e5c)" role="img" aria-label="GIF thumbnail: people at a party"></span>
    <span class="thumb" style="background:linear-gradient(135deg,#e59a2e,#7a3c12)" role="img" aria-label="GIF thumbnail: dancers at sunset"></span>
    <span class="thumb" style="background:linear-gradient(135deg,#f3e1d2,#d8b59a)" role="img" aria-label="GIF thumbnail: laughing baby"></span>
    <span class="thumb" style="background:linear-gradient(135deg,#8fb5d6,#3e5f86)" role="img" aria-label="GIF thumbnail: people celebrating"></span>
  </div>
  <span class="nav-arrow"><svg width="8" height="14"><polyline points="1,1 7,7 1,13" fill="none" stroke="#777" stroke-width="2"/></svg></span>
</div>

<div class="rule" style="top:600px"></div>

<h2 class="gallery-title" style="top:622px">TRENDING NOW</h2>
<div class="gallery-row" style="top:650px">
  <span class="nav-arrow"><svg width="8" height="14"><polyline points="7,1 1,7 7,13" fill="none" stroke="#777" stroke-width="2"/></svg></span>
  <div class="thumbs">
    <span class="thumb" style="background:linear-gradient(135deg,#2d3a2a,#7a8a5a)" role="img" aria-label="GIF thumbnail: figure in the dark"></span>
    <span class="thumb" style="background:linear-gradient(135deg,#a7c6dd,#e9eef2)" role="img" aria-label="GIF thumbnail: couple on a beach"></span>
    <span class="thumb" style="background:linear-gradient(135deg,#3d6b2a,#9fc25a)" role="img" aria-label="GIF thumbnail: forest scene"></span>
    <span class="thumb" style="background:linear-gradient(135deg,#c8281e,#6fa83b)" role="img" aria-label="GIF thumbnail: red flowers"></span>
    <span class="thumb" style="background:linear-gradient(135deg,#b08a5c,#e0c9a4)" role="img" aria-label="GIF thumbnail: small pet"></span>
  </div>
  <span class="nav-arrow"><svg width="8" height="14"><polyline points="1,1 7,7 1,13" fill="none" stroke="#777" stroke-width="2"/></svg></span>
</div>

<div class="rule" style="top:760px"></div>

<h2 class="gallery-title" style="top:782px">FAVOURITES</h2>
<div class="gallery-row" style="top:810px">
  <span class="nav-arrow"><svg width="8" height="14"><polyline points="7,1 1,7 7,13" fill="none" stroke="#777" stroke-width="2"/></svg></span>
  <div class="thumbs">
    <span class="thumb" style="background:linear-gradient(135deg,#3aa7c9,#e7c06a)" role="img" aria-label="GIF thumbnail: tropical beach"></span>
    <span class="thumb" style="background:linear-gradient(135deg,#7ea655,#2f4c24)" role="img" aria-label="GIF thumbnail: runner on a path"></span>
    <span class="thumb" style="background:linear-gradient(135deg,#f2d48c,#c9782c)" role="img" aria-label="GIF thumbnail: sunny field"></span>
    <span class="thumb" style="background:linear-gradient(135deg,#2c6fa3,#b8e1f2)" role="img" aria-label="GIF thumbnail: surfer on a wave"></span>
    <span class="thumb" style="background:linear-gradient(135deg,#e88a1c,#6b2b0c)" role="img" aria-label="GIF thumbnail: sunset silhouettes"></span>
  </div>
  <span class="nav-arrow"><svg width="8" height="14"><polyline points="1,1 7,7 1,13" fill="none" stroke="#777" stroke-width="2"/></svg></span>
</div>

<div class="rule" style="top:920px"></div>

<h2 class="gallery-title" style="top:952px">COMMENT</h2>
<div class="comment-box">
  <span class="avatar"></span>
  <div class="comment-input">Add a comment...</div>
  <p class="plugin-note">Chatterloft social plugin</p>
  <a class="btn-comment" href="#">COMMENT</a>
</div>

<footer class="site-footer">
  <nav class="footer-links">
    <a href="#">Upload a GIF</a><span class="sep">|</span><a href="#">Video to GIF</a><span class="sep">|</span><a href="#">Webcam to GIF</a><span class="sep">|</span><a href="#">VidTube to GIF</a><span class="sep">|</span><a href="#">Privacy Policy</a><span class="sep">|</span><a href="#">Contact Us</a><span class="sep">|</span><a href="#">Request Deletion</a>
  </nav>
  <div class="footer-bottom">
    <span>© 2013 SpinReel | All rights reserved</span>
    <div class="footer-social">
      <span style="background:var(--c1)" role="img" aria-label="Chatterloft"></span>
      <span style="background:var(--c2)" role="img" aria-label="Quillpost"></span>
      <span style="background:var(--c3)" role="img" aria-label="Orbitcircle"></span>
    </div>
  </div>
</footer>

</body>
</html>
```